LOLU Baby Massage Classes - flyer to make a difference

I need a single page flyer, preferably single page, to hand out to doctors, medical centres and parents. To also leave on counters of establishments.
It is to promote my baby massage classes. Mums can get together with other mums and book a 5 week course to learn and discover the many benefits of baby massage.
Benefits include: enhances bonding and attachment, understand non-verbal cues from your baby, helps with sleep patterns, help with immune system, increases vagal activity,relief from wind, colic or constipation to name some.

Baby age from birth to 12 months. Group classes or private sessions

I am a Professional Member and Certified by the Global Society of Newborn Touch (GSNT) GSNT Australia is Nationally Accredited and is endorsed by Crown Academy of Carers, the Southern Guild of Birth Attendants, The Southern Union of Daily Living Therapy Australia, The Southern Union of Bodywork Practitioner and is a full member of Wellmind Network Australia.

Class detail and availability contact is Petra Holm 0487 315 208 petra.joanne.holm@quillmail.example www.lolunewborntouch com.au facebook/comLOLUnewborntouch

My colour scheme is green and purple as you will see from my logo and website. I would like my flyer to be softer tones of either both colours or just one.

I will include some images you can choose from or show me any you think will fit in with baby massage. THANK YOU
Updates

Hi The size of my flyer is A6. Approx 150mms x 210mms and single sided. Thank you

Target Market(s)

mums and dads, groups, doctors, midwives

Industry/Entity Type

Medical

Font styles to use
Sans Serif

Colors
87d0c7
b09cc8

Requirements
Must have
• baby photo or photos, both my logo and the GSNT logo. The GSNT logo is to be small
• Baby Massage Classes (wording) is very important to catch the eye.
• Invitation to book a class or gather friends to book is next in importance
• Benefits is next
• The admin information ie.,membership, certification and endorsements are lesser and can be small.
• Contact information to be noticeable.
Nice to have
• If you have an idea, drawing or photo that would look better, please feel free to try it
Should not have
• should not be crowded with information all the same size

```html
<!DOCTYPE html>
<html lang="en">
<head>
<meta charset="utf-8">
<title>LOLU Baby Massage Classes</title>
<link href="https://fonts.googleapis.com/css2?family=Open+Sans:wght@300;400;600&display=swap" rel="stylesheet">
<style>
  :root {
    --teal: #1aa295;
    --teal-deep: #14968a;
    --purple: #922c8e;
    --purple-logo: #8c3d97;
    --white: #ffffff;
    --ink: #1e1e1e;
    --skin-light: #f4ece7;
    --skin-mid: #e6d3c8;
    --photo-bg: #f7f7f8;
  }
  html, body {
    margin: 0;
    padding: 0;
    overflow: hidden;
    background: var(--white);
  }
  .flyer {
    position: relative;
    width: 848px;
    height: 1200px;
    overflow: hidden;
    background: var(--white);
    font-family: "Open Sans", Arial, sans-serif;
    color: var(--ink);
  }
  .hero-photo {
    position: absolute;
    left: 0; top: 100px;
    width: 848px; height: 588px;
    background:
      radial-gradient(ellipse 260px 240px at 300px 210px, var(--skin-mid) 0%, var(--skin-light) 60%, transparent 100%),
      radial-gradient(ellipse 220px 260px at 720px 150px, var(--skin-mid) 0%, transparent 100%),
      linear-gradient(180deg, var(--photo-bg) 0%, #eceef0 100%);
  }
  .brand {
    position: absolute;
    left: 0; top: 0;
    width: 215px; height: 135px;
    background: var(--white);
    display: flex;
    align-items: center;
    justify-content: center;
    gap: 12px;
  }
  .brand-dot {
    width: 44px; height: 44px;
    border-radius: 50%;
    background: var(--teal);
  }
  .brand-name {
    font-size: 40px;
    font-weight: 600;
    color: var(--purple-logo);
    letter-spacing: 1px;
  }
  .headline {
    position: absolute;
    left: 317px; top: 0;
    width: 531px; height: 100px;
    background: var(--teal);
    color: var(--white);
    box-sizing: border-box;
    padding: 14px 0 0 16px;
  }
  .headline h1 {
    margin: 0;
    font-size: 41px;
    font-weight: 600;
    line-height: 50px;
    letter-spacing: 0.2px;
  }
  .headline p {
    margin: 4px 0 0;
    font-size: 15.5px;
    font-weight: 400;
  }
  .instructor-bar {
    position: absolute;
    left: 170px; top: 540px;
    width: 660px; height: 86px;
    background: var(--teal);
    border-radius: 0 43px 43px 0;
    color: var(--white);
    box-sizing: border-box;
    padding: 13px 26px 0 46px;
    font-size: 14.2px;
    line-height: 18px;
  }
  .instructor-bar strong {
    font-weight: 400;
    font-size: 17px;
  }
  .instructor-portrait {
    position: absolute;
    left: 22px; top: 486px;
    width: 192px; height: 192px;
    border-radius: 50%;
    background: var(--teal);
  }
  .instructor-portrait .photo {
    position: absolute;
    left: 14px; top: 14px;
    width: 164px; height: 164px;
    border-radius: 50%;
    background: radial-gradient(circle at 50% 40%, #c9b7a9 0%, #6f7d55 70%, #3d4a2c 100%);
  }
  .cert-badge {
    position: absolute;
    left: 232px; top: 496px;
    width: 28px; height: 28px;
    border-radius: 50%;
    background: var(--purple-logo);
    opacity: 0.75;
  }
  .benefits {
    position: absolute;
    left: 0; top: 688px;
    width: 848px; height: 200px;
    background: var(--purple);
    color: var(--white);
    text-align: center;
  }
  .benefits h2 {
    margin: 0;
    position: absolute;
    left: 212px; top: 8px;
    display: flex;
    align-items: center;
    gap: 12px;
    font-size: 68px;
    font-weight: 300;
    letter-spacing: 1px;
  }
  .benefits .rule {
    position: absolute;
    left: 42px; top: 87px;
    width: 766px; height: 1px;
    background: rgba(255,255,255,0.35);
  }
  .benefits p {
    position: absolute;
    left: 30px; top: 99px;
    width: 788px;
    margin: 0;
    font-size: 17.5px;
    line-height: 22px;
  }
  .booking {
    position: absolute;
    left: 0; top: 888px;
    width: 848px; height: 152px;
  }
  .booking .device-photo {
    position: absolute;
    left: 58px; top: 26px;
    width: 250px; height: 112px;
    background: linear-gradient(90deg, #cfd3d8 0%, #eadbd2 60%, #ffffff 100%);
    border-radius: 6px;
  }
  .booking h3 {
    position: absolute;
    left: 326px; top: 8px;
    margin: 0;
    font-size: 82px;
    font-weight: 300;
    line-height: 100px;
    color: var(--ink);
  }
  .booking p {
    position: absolute;
    left: 328px; top: 103px;
    margin: 0;
    font-size: 23px;
    font-weight: 400;
    color: #333;
  }
  .contact {
    position: absolute;
    left: 0; top: 1040px;
    width: 848px; height: 160px;
    background: var(--teal);
    color: var(--white);
    text-align: center;
  }
  .contact .phone {
    margin: 0;
    padding-top: 8px;
    font-size: 86px;
    font-weight: 300;
    line-height: 100px;
    letter-spacing: 2px;
  }
  .contact .details {
    margin: 2px 0 0;
    font-size: 17.5px;
    line-height: 23px;
  }
</style>
</head>
<body>
<main class="flyer">
  <div class="hero-photo" role="img" aria-label="Smiling baby lying on a white towel while a parent's hands massage the baby's chest"></div>

  <div class="brand">
    <span class="brand-dot"></span>
    <span class="brand-name">LOLU</span>
  </div>

  <header class="headline">
    <h1>BABY MASSAGE CLASSES</h1>
    <p>From birth to 12 months. Group classes or private sessions</p>
  </header>

  <div class="instructor-bar">
    <strong>Petra Holm</strong> : I am a Professional Member and Certified by the Global Society of Newborn Touch (GSNT) GSNT Australia is Nationally Accredited and is endorsed by Crown Academy of Carers, the Southern Guild of Birth Attendants,
  </div>
  <div class="instructor-portrait">
    <div class="photo" role="img" aria-label="Portrait photo of instructor Petra Holm"></div>
  </div>
  <div class="cert-badge" aria-hidden="true"></div>

  <section class="benefits">
    <h2>
      <svg width="52" height="44" viewBox="0 0 52 44" aria-hidden="true">
        <path d="M4 14 L14 24 L26 6 L38 24 L48 14 L44 34 L8 34 Z" fill="#fff"/>
        <rect x="8" y="37" width="36" height="5" fill="#fff"/>
        <circle cx="4" cy="12" r="3" fill="#fff"/>
        <circle cx="26" cy="4" r="3" fill="#fff"/>
        <circle cx="48" cy="12" r="3" fill="#fff"/>
      </svg>
      BENEFITS
    </h2>
    <div class="rule"></div>
    <p>enhances bonding and attachment, understand non-verbal cues from your baby, helps with sleep patterns, help with immune system, increases vagal activity,relief from wind, colic or constipation to name some.</p>
  </section>

  <section class="booking">
    <div class="device-photo" role="img" aria-label="Hand reaching towards a smartphone to book online"></div>
    <h3>book a class</h3>
    <p>or gather friends to book</p>
  </section>

  <footer class="contact">
    <p class="phone">0487 315 208</p>
    <p class="details">petra.joanne.holm@quillmail.example<br>www.lolunewborntouch com.au facebook/comLOLUnewborntouch</p>
  </footer>
</main>
</body>
</html>
```